Music School needs Calendar Design

Need Calendar design for a music school. Calendar is a small desktop calendar. Calendar is a flip calendar about 4" x 8" with a base. Very open-ended, just want something that's classy and simple. In the past we've used a theme, like 12 composers, 12 instruments, 12 styles of music, etc...

Industry/Entity Type

School

Font styles to use
Decorative

Requirements
Must have
• Will need to design calendar pages and base. Base fairly straightforward since it just contains contact info. There are some dates that need to be highlighted that are not national holidays

```html
<!DOCTYPE html>
<html lang="en">
<head>
<meta charset="utf-8">
<title>Music School Desk Calendar 2017</title>
<link rel="stylesheet" href="https://fonts.googleapis.com/css2?family=Caveat:wght@400;600&family=Courier+Prime&family=Gochi+Hand&family=Noto+Serif:wght@400&display=swap">
<style>
:root{
  --bg:#ffffff;
  --red:#ff0000;
  --page:#e9eaea;
  --edge:#b9bbbb;
  --card:#ffffff;
  --ink:#111111;
  --art-a:#f4f4f4;
  --art-b:#cfd0d0;
}
*{box-sizing:border-box;margin:0;padding:0}
html,body{width:1200px;height:1200px;overflow:hidden;background:var(--bg)}
.canvas{position:relative;width:1200px;height:1200px}

.page{position:absolute;width:254px;height:188px;background:var(--page);border:1px solid var(--edge);overflow:hidden}
.page__binding{position:absolute;left:6px;right:6px;top:6px;height:8px;
  background:repeating-linear-gradient(90deg,var(--ink) 0 6px,transparent 6px 9px)}
.page__band{position:absolute;left:0;right:0;top:20px;height:26px;background:var(--red);color:#fff}
.page__year{position:absolute;left:36px;top:0;font:400 22px/26px "Gochi Hand",cursive}
.page__month{position:absolute;right:40px;top:1px;font:400 15px/26px "Caveat",cursive}
.page__card{position:absolute;left:22px;top:64px;width:116px;height:100px;background:var(--card);
  box-shadow:0 3px 4px rgba(0,0,0,.18);padding:6px 6px 0}
.page__title{text-align:center;color:var(--red);font:400 9.5px/10px "Courier Prime",monospace;letter-spacing:.3px}
.days{display:grid;grid-template-columns:repeat(7,1fr);margin-top:3px;row-gap:4px;
  font:400 4.6px/5px "Noto Serif",serif;text-align:center;color:var(--ink)}
.days b{font-weight:400;font-size:3.8px;margin-bottom:1px}
.days > :nth-child(7n+1),.days > :nth-child(7n){color:var(--red)}
.days .pair{font-size:3.4px}
.page__art{position:absolute;left:150px;top:56px;width:94px;height:112px;
  background:radial-gradient(ellipse at 50% 55%,var(--art-a),var(--art-b))}
.page__footer{position:absolute;left:30px;right:12px;bottom:6px;font:400 5.4px/6px "Caveat",cursive;color:#333;white-space:nowrap}
.page__footer span{color:var(--red)}

.page--hero{left:322px;top:26px;transform:scale(2.2);transform-origin:0 0;box-shadow:0 1px 2px rgba(0,0,0,.15)}

.c1{left:46px}.c2{left:330px}.c3{left:614px}.c4{left:899px}
.r1{top:490px}.r2{top:720px}.r3{top:950px}
</style>
</head>
<body>
<div class="canvas">

<!-- Featured January page -->
<section class="page page--hero">
  <div class="page__binding"></div>
  <div class="page__band"><span class="page__year">2017</span><span class="page__month">January</span></div>
  <div class="page__card"><h3 class="page__title">January</h3>
    <div class="days"><b>Sun</b><b>Mon</b><b>Tue</b><b>Wed</b><b>Thu</b><b>Fri</b><b>Sat</b>
      <span>1</span><span>2</span><span>3</span><span>4</span><span>5</span><span>6</span><span>7</span><span>8</span><span>9</span><span>10</span><span>11</span><span>12</span><span>13</span><span>14</span><span>15</span><span>16</span><span>17</span><span>18</span><span>19</span><span>20</span><span>21</span><span>22</span><span>23</span><span>24</span><span>25</span><span>26</span><span>27</span><span>28</span><span>29</span><span>30</span><span>31</span></div></div>
  <div class="page__art" role="img" aria-label="Line illustration of two cats playing violin and piano"></div>
  <p class="page__footer">Adress: <span>lorem ipsum dolor sit amet, consectetur adipiscing</span> &nbsp;Telephone: <span>01 98 765 432 10</span></p>
</section>

<!-- January -->
<section class="page c1 r1">
  <div class="page__binding"></div>
  <div class="page__band"><span class="page__year">2017</span><span class="page__month">January</span></div>
  <div class="page__card"><h3 class="page__title">January</h3>
    <div class="days"><b>Sun</b><b>Mon</b><b>Tue</b><b>Wed</b><b>Thu</b><b>Fri</b><b>Sat</b>
      <span>1</span><span>2</span><span>3</span><span>4</span><span>5</span><span>6</span><span>7</span><span>8</span><span>9</span><span>10</span><span>11</span><span>12</span><span>13</span><span>14</span><span>15</span><span>16</span><span>17</span><span>18</span><span>19</span><span>20</span><span>21</span><span>22</span><span>23</span><span>24</span><span>25</span><span>26</span><span>27</span><span>28</span><span>29</span><span>30</span><span>31</span></div></div>
  <div class="page__art" role="img" aria-label="Line illustration of two cats playing violin and piano"></div>
</section>

<!-- February -->
<section class="page c2 r1">
  <div class="page__binding"></div>
  <div class="page__band"><span class="page__year">2017</span><span class="page__month">February</span></div>
  <div class="page__card"><h3 class="page__title">February</h3>
    <div class="days"><b>Sun</b><b>Mon</b><b>Tue</b><b>Wed</b><b>Thu</b><b>Fri</b><b>Sat</b>
      <i></i><i></i><i></i><span>1</span><span>2</span><span>3</span><span>4</span><span>5</span><span>6</span><span>7</span><span>8</span><span>9</span><span>10</span><span>11</span><span>12</span><span>13</span><span>14</span><span>15</span><span>16</span><span>17</span><span>18</span><span>19</span><span>20</span><span>21</span><span>22</span><span>23</span><span>24</span><span>25</span><span>26</span><span>27</span><span>28</span></div></div>
  <div class="page__art" role="img" aria-label="Line illustration of two birds playing guitar and trumpet"></div>
</section>

<!-- March -->
<section class="page c3 r1">
  <div class="page__binding"></div>
  <div class="page__band"><span class="page__year">2017</span><span class="page__month">March</span></div>
  <div class="page__card"><h3 class="page__title">March</h3>
    <div class="days"><b>Sun</b><b>Mon</b><b>Tue</b><b>Wed</b><b>Thu</b><b>Fri</b><b>Sat</b>
      <i></i><i></i><i></i><span>1</span><span>2</span><span>3</span><span>4</span><span>5</span><span>6</span><span>7</span><span>8</span><span>9</span><span>10</span><span>11</span><span>12</span><span>13</span><span>14</span><span>15</span><span>16</span><span>17</span><span>18</span><span>19</span><span>20</span><span>21</span><span>22</span><span>23</span><span>24</span><span>25</span><span>26</span><span>27</span><span>28</span><span>29</span><span>30</span><span>31</span></div></div>
  <div class="page__art" role="img" aria-label="Line illustration of a boy playing trumpet"></div>
</section>

<!-- April -->
<section class="page c4 r1">
  <div class="page__binding"></div>
  <div class="page__band"><span class="page__year">2017</span><span class="page__month">April</span></div>
  <div class="page__card"><h3 class="page__title">April</h3>
    <div class="days"><b>Sun</b><b>Mon</b><b>Tue</b><b>Wed</b><b>Thu</b><b>Fri</b><b>Sat</b>
      <i></i><i></i><i></i><i></i><i></i><i></i><span>1</span><span>2</span><span>3</span><span>4</span><span>5</span><span>6</span><span>7</span><span>8</span><span>9</span><span>10</span><span>11</span><span>12</span><span>13</span><span>14</span><span>15</span><span>16</span><span>17</span><span>18</span><span>19</span><span>20</span><span>21</span><span>22</span><span class="pair">23/30</span><span>24</span><span>25</span><span>26</span><span>27</span><span>28</span><span>29</span></div></div>
  <div class="page__art" role="img" aria-label="Line illustration of three children singing in a bathtub"></div>
</section>

<!-- May -->
<section class="page c1 r2">
  <div class="page__binding"></div>
  <div class="page__band"><span class="page__year">2017</span><span class="page__month">May</span></div>
  <div class="page__card"><h3 class="page__title">May</h3>
    <div class="days"><b>Sun</b><b>Mon</b><b>Tue</b><b>Wed</b><b>Thu</b><b>Fri</b><b>Sat</b>
      <i></i><span>1</span><span>2</span><span>3</span><span>4</span><span>5</span><span>6</span><span>7</span><span>8</span><span>9</span><span>10</span><span>11</span><span>12</span><span>13</span><span>14</span><span>15</span><span>16</span><span>17</span><span>18</span><span>19</span><span>20</span><span>21</span><span>22</span><span>23</span><span>24</span><span>25</span><span>26</span><span>27</span><span>28</span><span>29</span><span>30</span><span>31</span></div></div>
  <div class="page__art" role="img" aria-label="Line illustration of a small band playing drums and guitar on a sofa"></div>
</section>

<!-- June -->
<section class="page c2 r2">
  <div class="page__binding"></div>
  <div class="page__band"><span class="page__year">2017</span><span class="page__month">June</span></div>
  <div class="page__card"><h3 class="page__title">June</h3>
    <div class="days"><b>Sun</b><b>Mon</b><b>Tue</b><b>Wed</b><b>Thu</b><b>Fri</b><b>Sat</b>
      <i></i><i></i><i></i><i></i><span>1</span><span>2</span><span>3</span><span>4</span><span>5</span><span>6</span><span>7</span><span>8</span><span>9</span><span>10</span><span>11</span><span>12</span><span>13</span><span>14</span><span>15</span><span>16</span><span>17</span><span>18</span><span>19</span><span>20</span><span>21</span><span>22</span><span>23</span><span>24</span><span>25</span><span>26</span><span>27</span><span>28</span><span>29</span><span>30</span></div></div>
  <div class="page__art" role="img" aria-label="Line illustration of two dogs dancing"></div>
</section>

<!-- July -->
<section class="page c3 r2">
  <div class="page__binding"></div>
  <div class="page__band"><span class="page__year">2017</span><span class="page__month">July</span></div>
  <div class="page__card"><h3 class="page__title">July</h3>
    <div class="days"><b>Sun</b><b>Mon</b><b>Tue</b><b>Wed</b><b>Thu</b><b>Fri</b><b>Sat</b>
      <i></i><i></i><i></i><i></i><i></i><i></i><span>1</span><span>2</span><span>3</span><span>4</span><span>5</span><span>6</span><span>7</span><span>8</span><span>9</span><span>10</span><span>11</span><span>12</span><span>13</span><span>14</span><span>15</span><span>16</span><span>17</span><span>18</span><span>19</span><span>20</span><span>21</span><span>22</span><span class="pair">23/30</span><span class="pair">24/31</span><span>25</span><span>26</span><span>27</span><span>28</span><span>29</span></div></div>
  <div class="page__art" role="img" aria-label="Line illustration of a cat in sunglasses playing violin"></div>
</section>

<!-- August -->
<section class="page c4 r2">
  <div class="page__binding"></div>
  <div class="page__band"><span class="page__year">2017</span><span class="page__month">August</span></div>
  <div class="page__card"><h3 class="page__title">August</h3>
    <div class="days"><b>Sun</b><b>Mon</b><b>Tue</b><b>Wed</b><b>Thu</b><b>Fri</b><b>Sat</b>
      <i></i><i></i><span>1</span><span>2</span><span>3</span><span>4</span><span>5</span><span>6</span><span>7</span><span>8</span><span>9</span><span>10</span><span>11</span><span>12</span><span>13</span><span>14</span><span>15</span><span>16</span><span>17</span><span>18</span><span>19</span><span>20</span><span>21</span><span>22</span><span>23</span><span>24</span><span>25</span><span>26</span><span>27</span><span>28</span><span>29</span><span>30</span><span>31</span></div></div>
  <div class="page__art" role="img" aria-label="Line illustration of a duck playing banjo"></div>
</section>

<!-- September -->
<section class="page c1 r3">
  <div class="page__binding"></div>
  <div class="page__band"><span class="page__year">2017</span><span class="page__month">September</span></div>
  <div class="page__card"><h3 class="page__title">September</h3>
    <div class="days"><b>Sun</b><b>Mon</b><b>Tue</b><b>Wed</b><b>Thu</b><b>Fri</b><b>Sat</b>
      <i></i><i></i><i></i><i></i><i></i><span>1</span><span>2</span><span>3</span><span>4</span><span>5</span><span>6</span><span>7</span><span>8</span><span>9</span><span>10</span><span>11</span><span>12</span><span>13</span><span>14</span><span>15</span><span>16</span><span>17</span><span>18</span><span>19</span><span>20</span><span>21</span><span>22</span><span>23</span><span>24</span><span>25</span><span>26</span><span>27</span><span>28</span><span>29</span><span>30</span></div></div>
  <div class="page__art" role="img" aria-label="Line illustration of a marching drummer with trumpet"></div>
</section>

<!-- October -->
<section class="page c2 r3">
  <div class="page__binding"></div>
  <div class="page__band"><span class="page__year">2017</span><span class="page__month">October</span></div>
  <div class="page__card"><h3 class="page__title">October</h3>
    <div class="days"><b>Sun</b><b>Mon</b><b>Tue</b><b>Wed</b><b>Thu</b><b>Fri</b><b>Sat</b>
      <span>1</span><span>2</span><span>3</span><span>4</span><span>5</span><span>6</span><span>7</span><span>8</span><span>9</span><span>10</span><span>11</span><span>12</span><span>13</span><span>14</span><span>15</span><span>16</span><span>17</span><span>18</span><span>19</span><span>20</span><span>21</span><span>22</span><span>23</span><span>24</span><span>25</span><span>26</span><span>27</span><span>28</span><span>29</span><span>30</span><span>31</span></div></div>
  <div class="page__art" role="img" aria-label="Line illustration of a fiddler and a dancing cat"></div>
</section>

<!-- November -->
<section class="page c3 r3">
  <div class="page__binding"></div>
  <div class="page__band"><span class="page__year">2017</span><span class="page__month">November</span></div>
  <div class="page__card"><h3 class="page__title">November</h3>
    <div class="days"><b>Sun</b><b>Mon</b><b>Tue</b><b>Wed</b><b>Thu</b><b>Fri</b><b>Sat</b>
      <i></i><i></i><i></i><span>1</span><span>2</span><span>3</span><span>4</span><span>5</span><span>6</span><span>7</span><span>8</span><span>9</span><span>10</span><span>11</span><span>12</span><span>13</span><span>14</span><span>15</span><span>16</span><span>17</span><span>18</span><span>19</span><span>20</span><span>21</span><span>22</span><span>23</span><span>24</span><span>25</span><span>26</span><span>27</span><span>28</span><span>29</span><span>30</span></div></div>
  <div class="page__art" role="img" aria-label="Line illustration of two violinists playing together"></div>
</section>

<!-- December -->
<section class="page c4 r3">
  <div class="page__binding"></div>
  <div class="page__band"><span class="page__year">2017</span><span class="page__month">December</span></div>
  <div class="page__card"><h3 class="page__title">December</h3>
    <div class="days"><b>Sun</b><b>Mon</b><b>Tue</b><b>Wed</b><b>Thu</b><b>Fri</b><b>Sat</b>
      <i></i><i></i><i></i><i></i><i></i><span>1</span><span>2</span><span>3</span><span>4</span><span>5</span><span>6</span><span>7</span><span>8</span><span>9</span><span>10</span><span>11</span><span>12</span><span>13</span><span>14</span><span>15</span><span>16</span><span>17</span><span>18</span><span>19</span><span>20</span><span>21</span><span>22</span><span>23</span><span class="pair">24/31</span><span>25</span><span>26</span><span>27</span><span>28</span><span>29</span><span>30</span></div></div>
  <div class="page__art" role="img" aria-label="Line illustration of three children singing a carol"></div>
</section>

</div>
</body>
</html>
```